PowerGrind Flyer

I need a flyer for a new PowerGrind gym I am starting.
I would like our logo some where on the flyer.
PowerGrind is functional movement, performed at a high intensity, that is constantly varied
PowerGrind is designed to get you in the best shape of your life no matter what your age.
The "Charter Circle" (first 40 people to signup) will receive a $30 discount for their first 3 months of PowerGrind and a Charter Tee.
Call Darrel at 555-318-2046 for details
Email us at 4570powergrind@mailnest.example
Facebook 4570 PowerGrind Halvern
Opening December 1st
Location 417 Birchmont St
Prices starting at $79/month
Updates

the flyer will be printed on 8.5 x 11 paper and one sided

Industry/Entity Type

Gym

```html
<!DOCTYPE html>
<html lang="en">
<head>
<meta charset="utf-8">
<title>45:70 PowerGrind Ferrum Vitae — Opening Flyer</title>
<link rel="stylesheet" href="https://fonts.googleapis.com/css2?family=Roboto:wght@300;400;500;700;900&display=swap">
<style>
  :root {
    --red-deep: #8e0a10;
    --red-main: #c8141c;
    --red-bright: #e0262c;
    --red-text: #a3161c;
    --white: #ffffff;
    --band-top: #ececec;
    --band-bottom: #d9d9d9;
    --ink-soft: #8a1a1e;
  }
  * { margin: 0; padding: 0; box-sizing: border-box; }
  html, body { width: 855px; height: 1200px; overflow: hidden; background: #fff; }
  body { font-family: 'Roboto', Arial, sans-serif; }

  .flyer {
    position: relative;
    width: 855px;
    height: 1200px;
    overflow: hidden;
    background: radial-gradient(ellipse at 62% 45%, var(--red-bright) 0%, var(--red-main) 45%, var(--red-deep) 100%);
  }

  /* Title block with corner brackets */
  .title-block {
    position: absolute;
    left: 130px; top: 62px;
    width: 615px; height: 183px;
    color: var(--white);
    text-align: center;
  }
  .title-block .bracket { position: absolute; inset: 0; }
  .title-line-1 {
    position: absolute; left: 0; right: 0; top: 30px;
    font-size: 62px; font-weight: 500; line-height: 1; letter-spacing: 0.5px;
  }
  .title-line-2 {
    position: absolute; left: 0; right: 0; top: 104px;
    font-size: 64px; font-weight: 500; line-height: 1; letter-spacing: 1px;
  }

  /* Price burst */
  .price-burst {
    position: absolute; left: 47px; top: 373px;
    width: 210px; height: 210px;
  }
  .price-burst svg { position: absolute; inset: 0; }
  .price-text {
    position: absolute; inset: 0;
    display: flex; flex-direction: column; align-items: center; justify-content: center;
    color: #1a1a1a;
  }
  .price-from { font-size: 21px; font-weight: 400; line-height: 1; margin-right: 28px; }
  .price-amount { font-size: 62px; font-weight: 700; line-height: 1; letter-spacing: -1px; }
  .price-period { font-size: 15px; font-weight: 400; line-height: 1; margin-left: 40px; }

  /* Athlete photo area */
  .athlete-photo {
    position: absolute; left: 318px; top: 295px;
    width: 537px; height: 660px;
    border-radius: 46% 46% 0 0 / 22% 22% 0 0;
    background: linear-gradient(180deg, #c98b5f 0%, #b8764c 55%, #8a5636 82%, #1e1a1a 100%);
    opacity: 0.9;
  }

  /* Benefit bullets */
  .benefits {
    position: absolute; left: 62px; top: 664px;
    list-style: none; color: var(--white);
  }
  .benefit { position: relative; padding-left: 40px; margin-bottom: 12px; }
  .benefit svg { position: absolute; left: 0; top: 16px; }
  .benefit-line { display: block; font-size: 47px; line-height: 46px; }
  .strong { font-weight: 700; }
  .light { font-weight: 300; }

  /* Information band */
  .info-band {
    position: absolute; left: 0; top: 955px;
    width: 855px; height: 245px;
    background: linear-gradient(180deg, var(--band-top), var(--band-bottom));
  }
  .charter-offer {
    position: absolute; left: 30px; top: 12px; width: 370px;
    font-size: 26px; line-height: 33px; font-weight: 400; color: var(--red-text);
  }
  .charter-offer b { font-weight: 700; }

  .brand-mark {
    position: absolute; left: 418px; top: 28px; width: 142px;
    display: flex; flex-direction: column; align-items: center; gap: 10px;
  }
  .brand-square { width: 50px; height: 50px; background: var(--red-text); }
  .brand-name {
    font-size: 16px; font-weight: 700; color: var(--red-text);
    text-align: center; line-height: 1.2;
  }

  .opening-details {
    position: absolute; left: 563px; top: 50px;
    color: var(--red-text); font-weight: 700;
  }
  .opening-details p { font-size: 22px; line-height: 1; margin-bottom: 25px; }
  .opening-details .address { font-size: 20px; }

  .contact-row {
    position: absolute; left: 28px; top: 180px; right: 20px;
    display: flex; align-items: center; justify-content: space-between;
    font-size: 17px; color: var(--ink-soft);
  }
  .contact-item { display: flex; align-items: center; gap: 8px; white-space: nowrap; }
  .social-square { width: 22px; height: 22px; background: var(--red-text); border-radius: 3px; }
</style>
</head>
<body>
<main class="flyer">

  <header class="title-block">
    <svg class="bracket" width="615" height="183" viewBox="0 0 615 183" aria-hidden="true">
      <g fill="none" stroke="#ffffff" stroke-width="6">
        <polyline points="3,40 3,3 45,3"/>
        <polyline points="570,3 612,3 612,40"/>
        <polyline points="3,140 3,180 45,180"/>
        <polyline points="570,180 612,180 612,140"/>
      </g>
    </svg>
    <h1>
      <span class="title-line-1">45:70POWERGRIND</span>
      <span class="title-line-2">FERRUM VITAE</span>
    </h1>
  </header>

  <div class="price-burst">
    <svg width="210" height="210" viewBox="0 0 210 210" aria-hidden="true">
      <defs>
        <radialGradient id="burstFill" cx="50%" cy="45%" r="60%">
          <stop offset="0%" stop-color="#ffffff"/>
          <stop offset="70%" stop-color="#ededed"/>
          <stop offset="100%" stop-color="#bdbdbd"/>
        </radialGradient>
      </defs>
      <polygon fill="url(#burstFill)" points="105.0,0.0 113.2,15.2 125.5,2.9 129.9,19.6 145.2,11.0 145.0,28.2 161.8,24.3 157.0,40.8 174.2,41.3 165.0,55.9 181.7,61.0 169.3,73.0 184.6,82.2 169.3,92.0 182.0,105.0 169.3,118.0 184.6,127.8 169.3,137.0 181.7,149.0 165.0,154.1 174.2,168.7 157.0,169.2 161.8,185.7 145.0,181.8 145.2,199.0 129.9,190.4 125.5,207.1 113.2,194.8 105.0,210.0 96.8,194.8 84.5,207.1 80.1,190.4 64.8,199.0 65.0,181.8 48.2,185.7 53.0,169.2 35.8,168.7 45.0,154.1 28.3,149.0 40.7,137.0 25.4,127.8 40.7,118.0 28.0,105.0 40.7,92.0 25.4,82.2 40.7,73.0 28.3,61.0 45.0,55.9 35.8,41.3 53.0,40.8 48.2,24.3 65.0,28.2 64.8,11.0 80.1,19.6 84.5,2.9 96.8,15.2"/>
    </svg>
    <div class="price-text">
      <span class="price-from">FROM</span>
      <span class="price-amount">$79</span>
      <span class="price-period">/MONTH</span>
    </div>
  </div>

  <div class="athlete-photo" role="img" aria-label="Photo of a shirtless, muscular athlete in black shorts looking upward"></div>

  <ul class="benefits">
    <li class="benefit">
      <svg width="14" height="20" viewBox="0 0 14 20" aria-hidden="true"><polyline points="2,2 11,10 2,18" fill="none" stroke="#fff" stroke-width="2.5"/></svg>
      <span class="benefit-line"><span class="strong">BEST</span> <span class="light">SHAPE</span></span>
    </li>
    <li class="benefit">
      <svg width="14" height="20" viewBox="0 0 14 20" aria-hidden="true"><polyline points="2,2 11,10 2,18" fill="none" stroke="#fff" stroke-width="2.5"/></svg>
      <span class="benefit-line strong">HIGH</span>
      <span class="benefit-line light">INTENSITY</span>
    </li>
    <li class="benefit">
      <svg width="14" height="20" viewBox="0 0 14 20" aria-hidden="true"><polyline points="2,2 11,10 2,18" fill="none" stroke="#fff" stroke-width="2.5"/></svg>
      <span class="benefit-line strong">FOR ALL</span>
      <span class="benefit-line light">AGES</span>
    </li>
  </ul>

  <section class="info-band">
    <p class="charter-offer"><b>$30 Discount</b> for the first 3 months and a Charter Tee if you are the first 40 people to sign up.</p>

    <div class="brand-mark">
      <span class="brand-square" aria-hidden="true"></span>
      <span class="brand-name">45:70 PowerGrind Ferrum Vitae</span>
    </div>

    <div class="opening-details">
      <p>Opening December 1st</p>
      <p class="address">Location 417 Birchmont St</p>
    </div>

    <div class="contact-row">
      <span class="contact-item"><span class="social-square" aria-hidden="true"></span>4570 PowerGrind Halvern</span>
      <span class="contact-item">
        <svg width="22" height="22" viewBox="0 0 24 24" aria-hidden="true"><path fill="#a3161c" d="M6.6 10.8a15.1 15.1 0 0 0 6.6 6.6l2.2-2.2a1 1 0 0 1 1-.25 11.4 11.4 0 0 0 3.6.57 1 1 0 0 1 1 1V20a1 1 0 0 1-1 1A17 17 0 0 1 3 4a1 1 0 0 1 1-1h3.5a1 1 0 0 1 1 1c0 1.25.2 2.45.57 3.57a1 1 0 0 1-.25 1z"/></svg>
        Call Darrel at 555-318-2046
      </span>
      <span class="contact-item">
        <svg width="24" height="18" viewBox="0 0 24 18" aria-hidden="true"><rect x="0" y="0" width="24" height="18" fill="#a3161c"/><polyline points="1,1 12,10 23,1" fill="none" stroke="#e3e3e3" stroke-width="2"/></svg>
        4570powergrind@mailnest.example
      </span>
    </div>
  </section>

</main>
</body>
</html>
```